Website for new dental office

I am Dr. Colin Marsh and am building a new dental practice. I specialize in general dentistry. I am young and have a higher end dental practice incorporating very new technologies and would like my website to reflect that. As many dental patients are older, the website must be very easy to navigate. I would like patients to be able to request appointments, and will eventually add on patient information forms (the health history, etc, that you normally fill out in the practice) from my practice management software, so leave an area for that.

Industry/Entity Type

Building

```html
<!DOCTYPE html>
<html lang="en">
<head>
<meta charset="utf-8">
<title>Marsh Dental</title>
<link href="https://fonts.googleapis.com/css2?family=Ubuntu:wght@400;500;700&family=Arimo:ital,wght@0,400;1,400&display=swap" rel="stylesheet">
<style>
:root{
  --teal:#0e8b80;
  --teal-dark:#0a6f66;
  --teal-light:#2aa89b;
  --navy:#13335f;
  --paper:#e4e4e4;
  --white:#ffffff;
  --ink:#2b2b2b;
  --muted:#9a9a9a;
  --footer:#252525;
  --footer-top:#161616;
  --green:#6cc12b;
  --star:#f07b12;
  --date:#1b5aa0;
}
*{margin:0;padding:0;box-sizing:border-box}
html,body{width:999px;height:1200px;overflow:hidden}
body{position:relative;background:var(--paper);font-family:"Arimo",Arial,sans-serif;color:var(--ink)}
.abs{position:absolute}

.top-strip{left:0;top:0;width:999px;height:8px;background:var(--teal)}
.header{left:0;top:8px;width:999px;height:75px;background:var(--white)}
.brand{display:flex;align-items:center;gap:10px}
.brand-dot{width:40px;height:40px;border-radius:50%;background:var(--teal);flex:none}
.brand-name{font-family:"Ubuntu",sans-serif;font-weight:500;font-size:26px;line-height:25px;color:var(--navy)}
.brand-top{left:83px;top:17px}
.brand-body{left:83px;top:560px}

.contact-box{left:659px;top:8px;width:256px;height:47px;background:var(--teal);border-radius:0 0 4px 4px;display:flex;color:var(--white);font-family:"Ubuntu",sans-serif}
.contact-box .cell{flex:1;padding:6px 0 0 13px;line-height:17px}
.contact-box .cell+.cell{border-left:1px solid rgba(255,255,255,.35);padding-left:14px}
.contact-box small{display:block;font-size:12px}
.contact-box strong{font-weight:500;font-size:15px}

.nav{left:0;top:83px;width:999px;height:39px;background:var(--teal);border-bottom:2px solid var(--white)}
.nav ul{list-style:none;display:flex;margin-left:83px}
.nav li{width:71px;height:37px;line-height:37px;font-family:"Ubuntu",sans-serif;font-size:10.5px;color:var(--white);padding-left:12px;border-right:1px solid rgba(255,255,255,.55)}
.nav li:nth-child(8){width:71px}
.nav li:last-child{border-right:none}

.hero{left:0;top:124px;width:999px;height:420px;background:radial-gradient(ellipse at 50% 40%,var(--teal-light),var(--teal) 70%,var(--teal-dark))}
.hero-frame{left:83px;top:142px;width:832px;height:347px;background:var(--white);padding:8px;box-shadow:0 10px 18px rgba(0,0,0,.25)}
.hero-photo{width:100%;height:100%;background:linear-gradient(110deg,#cfe3ef 0%,#2f6fc4 40%,#e9eef2 70%,#c9ced4 100%)}
.band-gap{left:0;top:544px;width:999px;height:5px;background:var(--white)}

.appt-btn{left:641px;top:560px;width:227px;height:66px;border-radius:5px;background:linear-gradient(#a6e05a,var(--green));border:2px solid #fff;box-shadow:0 1px 4px rgba(0,0,0,.3);font-family:"Ubuntu",sans-serif;color:#fff;padding:12px 0 0 18px}
.appt-btn span{display:block;font-size:13px;line-height:14px}
.appt-btn b{display:block;font-size:21px;font-weight:700;color:#1f3d10;letter-spacing:-.5px}
.appt-btn .clock{position:absolute;right:4px;top:3px;width:56px;height:56px;border-radius:50%;background:#fff;border:3px solid #c9c9c9}

.dots{left:108px;top:635px;width:766px;border-top:1px dotted #a8a8a8}
.intro-frame{left:83px;top:644px;width:174px;height:155px;background:var(--white);padding:6px;box-shadow:0 1px 4px rgba(0,0,0,.2)}
.intro-photo{width:100%;height:100%;background:linear-gradient(120deg,#e8e3de 0%,#1d7d6d 45%,#eadad0 100%)}
.intro-text{left:285px;top:651px;width:590px;font-family:"Ubuntu",sans-serif;font-size:10.8px;line-height:16.6px;text-align:justify;color:#333}
.intro-text p+p{margin-top:16.6px}
.intro-text em{font-style:italic;font-weight:500}
.rule{left:75px;top:830px;width:810px;height:3px;background:linear-gradient(90deg,transparent,#c4c4c4,transparent)}

.col-title{font-family:"Arimo",sans-serif;font-size:18px;color:var(--teal-dark)}
.col-frame{width:234px;height:102px;background:var(--white);padding:6px;box-shadow:0 1px 4px rgba(0,0,0,.2)}
.photo-a{width:100%;height:100%;background:linear-gradient(100deg,#dcdcdc,#2a4aa0 40%,#f2d8c8 75%,#e9e9e9)}
.photo-b{width:100%;height:100%;background:linear-gradient(100deg,#c9c3b3,#e6e2dc 40%,#3d6fb0 80%,#d4d8de)}
.col-text{width:221px;font-size:10.6px;line-height:16.6px;text-align:justify}
.vline{width:1px;height:220px;top:874px;background:#cfcfcf}

.testi h4{font-family:"Ubuntu",sans-serif;font-weight:500;font-size:13px;color:#222}
.stars{display:flex;gap:2px;margin:7px 0 4px}
.testi .date{font-style:italic;font-size:8.6px;color:var(--date)}
.testi p{font-size:9.6px;line-height:15px;color:#222}
.testi-sep{left:660px;top:991px;width:213px;border-top:1px dotted #b0b0b0}

.footer{left:0;top:1115px;width:999px;height:85px;background:var(--footer);border-top:7px solid var(--footer-top)}
.connected{left:93px;top:1134px;font-family:"Ubuntu",sans-serif;font-weight:500;font-size:13.5px;color:#ccc}
.socials{left:86px;top:1158px;display:flex;gap:5px}
.socials span{width:28px;height:28px;border-radius:50%;border:2px solid #ddd}
.fdiv{top:1128px;height:62px;border-left:1px dotted #555}
.flinks{left:293px;top:1140px;width:385px;text-align:center;font-size:10.4px;color:#ddd;letter-spacing:.3px}
.fcopy{left:293px;top:1162px;width:385px;text-align:center;font-size:10.4px;color:#aaa}
.fcontact{left:718px;top:1135px;font-size:10.4px;line-height:18.5px;color:#aaa}
.fcontact a{color:#777;text-decoration:none}
</style>
</head>
<body>
<div class="abs top-strip"></div>
<header class="abs header"></header>
<div class="abs brand brand-top"><span class="brand-dot"></span><span class="brand-name">Marsh<br>Dental</span></div>

<div class="abs contact-box">
  <div class="cell">
    <small><svg width="8" height="10" viewBox="0 0 8 10"><path d="M2 0h2l1 3-1.5 1c.5 1.5 1.3 2.4 2.5 3L7 6l1 2v2C4 10 0 6 0 2z" fill="#fff"/></svg> Contact us</small>
    <strong>555-210-4470</strong>
  </div>
  <div class="cell">
    <small>Make an</small>
    <strong>Appointment</strong>
  </div>
</div>

<nav class="abs nav">
  <ul>
    <li>HOME</li><li>TEAM</li><li>OFFICE</li><li>SERVICES</li><li>FORMS</li><li>GALLERY</li><li>REVIEWS</li><li>FAQS</li><li>CONTACT</li>
  </ul>
</nav>

<section class="abs hero"></section>
<div class="abs hero-frame"><div class="hero-photo" role="img" aria-label="Dentist in a modern treatment room with a patient, digital scans on screens"></div></div>
<div class="abs band-gap"></div>

<div class="abs brand brand-body"><span class="brand-dot"></span><span class="brand-name">Marsh<br>Dental</span></div>
<div class="abs appt-btn"><span>Click Here to Make an</span><b>APPOINTMENT</b>
  <svg class="clock" viewBox="0 0 56 56"><circle cx="28" cy="28" r="25" fill="#fff"/><path d="M28 28 L22 40 M28 28 L36 14 M28 28 L40 36" stroke="#222" stroke-width="1.6"/></svg>
</div>
<div class="abs dots"></div>

<div class="abs intro-frame"><div class="intro-photo" role="img" aria-label="Dentist in scrubs greeting a smiling patient in the chair"></div></div>
<div class="abs intro-text">
  <p><em>Lorem ipsum dolor sit amet, consectetuer adipiscing elit. Nam cursus. Morbi ut mi. Nullam enim leo, egestas</em> id, condimentum at, laoreet mattis, massa. Sed eleifend nonummy diam. Praesent mauris ante, elementum et, bibendum at, posuere sit amet, nibh. Duis tincidunt lectus quis dui viverra vestibulum. Suspendisse vulputate aliquam dui. Nulla elementum dui ut augue. Aliquam vehicula mi at mauris.</p>
  <p>Morbi magna magna, tincidunt a, mattis non, imperdiet vitae, tellus. Sed odio est, auctor ac, sollicitudin in, consequat vitae, orci. Fusce id felis. Vivamus sollicitudin metus eget eros.</p>
</div>
<div class="abs rule"></div>

<h3 class="abs col-title" style="left:83px;top:866px">Lorem Ipsum</h3>
<div class="abs col-frame" style="left:83px;top:898px"><div class="photo-a" role="img" aria-label="Dentist examining a patient's teeth"></div></div>
<p class="abs col-text" style="left:90px;top:1011px">Pellentesque habitant morbi tristique senectus et netus et malesuada fames ac turpis egestas. In posuere felis nec tortor.</p>
<div class="abs vline" style="left:342px"></div>

<h3 class="abs col-title" style="left:366px;top:868px">Lorem Ipsum</h3>
<div class="abs col-frame" style="left:367px;top:898px"><div class="photo-b" role="img" aria-label="Doctor explaining a spine model to a patient"></div></div>
<p class="abs col-text" style="left:374px;top:1010px">Pellentesque habitant morbi tristique senectus et netus et malesuada fames ac turpis egestas. In posuere felis nec tortor.</p>
<div class="abs vline" style="left:625px"></div>

<h3 class="abs col-title" style="left:659px;top:866px">Testimonials</h3>
<div class="abs testi" style="left:661px;top:893px;width:215px">
  <h4>Thanks for the treatment</h4>
  <div class="stars"><svg width="70" height="12" viewBox="0 0 70 12"><g fill="var(--star)"><path id="s" d="M6 0l1.8 4 4.2.3-3.2 2.7 1 4.2L6 9 2.2 11.2l1-4.2L0 4.3 4.2 4z"/><use href="#s" x="14"/><use href="#s" x="28"/><use href="#s" x="42"/><use href="#s" x="56"/></g></svg></div>
  <div class="date">May 12, 2013 by Priya</div>
  <p>Pellentesque habitant morbi tristique senectus et netus...</p>
</div>
<div class="abs testi-sep"></div>
<div class="abs testi" style="left:661px;top:1002px;width:215px">
  <h4>Ut accumsan ultricies elit</h4>
  <div class="stars" style="margin-top:4px"><svg width="70" height="12" viewBox="0 0 70 12"><g fill="var(--star)"><use href="#s"/><use href="#s" x="14"/><use href="#s" x="28"/><use href="#s" x="42"/><use href="#s" x="56"/></g></svg></div>
  <div class="date">May 12, 2013 by Priya</div>
  <p>Pellentesque habitant morbi tristique senectus et netus...</p>
</div>

<footer class="abs footer"></footer>
<div class="abs connected">Get Connected</div>
<div class="abs socials">
  <span style="background:#3b5998"></span><span style="background:#2aa3d8"></span><span style="background:#555"></span><span style="background:#f26b1d"></span><span style="background:#888"></span>
</div>
<div class="abs fdiv" style="left:293px"></div>
<div class="abs flinks">Home &nbsp;|&nbsp; About Us &nbsp;|&nbsp; Services &nbsp;|&nbsp; Testimonials &nbsp;|&nbsp; Contact Us</div>
<div class="abs fcopy">Copyright 2014 &nbsp;Marsh Dental</div>
<div class="abs fdiv" style="left:678px"></div>
<div class="abs fcontact">Telephone: 03 5550 1234<br>Mobile: 0400 555 219<br>Email: <a>info@marshdental.example</a></div>
</body>
</html>
```